Tarjetas de visita para empresa de aluminio

Empresa con mas de 40 años vendiendo perfiles de aluminio.
Somos fábrica y almacén, queremos renovar la tarjeta de presentación de nuestros comerciales dando una imgen innovadora y tecnógica mezclado con la calidez del respeto al medio ambiente.
Añado el logo de la empresa y actual cara trasera de la tarjeta de visita, el logo es el simbolo WM y la marca TRAVENIC EXTRUSION, la frase 2extrusion y lacado de aluminio" debe cambiarse por "Diseño, extrusión, lacado, anodizado y mecanizado de precisión de aluminio" o en su defecto incluir todos esos servicios que hacemos o una frase mas pegadiza.

We are an aluminium factory, we produce and stock profiles of aluminium.
we want to renew visit card of our sellers, we are looking for something that show innovation, tecnology and environment respect.
Upload our actual logo and back of visit card, logo WM and brand TRAVENIC EXTRUSION must be keept.
Text "Extrusion y lacado de aluminio" must be changed for "Diseño, extrusion, lacado, anodizado y mecanizado de precisión de aluminio" or something like that

```html
<!DOCTYPE html>
<html lang="es">
<head>
<meta charset="utf-8">
<title>Tarjeta de visita – Travenic Extrusion</title>
<link rel="stylesheet" href="https://fonts.googleapis.com/css2?family=Open+Sans:wght@400;700&family=Arimo:wght@400&display=swap">
<style>
  :root {
    --backdrop: #8a8a88;
    --card-white: #ffffff;
    --brand-blue: #22527a;
    --name-blue: #1f4a7a;
    --text-grey: #6b6b6b;
    --icon-blue: #2a5a8a;
    --on-blue: #ffffff;
    --silver: #e4e8ec;
  }
  * { box-sizing: border-box; margin: 0; padding: 0; }
  html, body {
    width: 1200px; height: 801px; overflow: hidden;
    background: var(--backdrop);
  }
  .stage {
    width: 1200px; height: 801px;
    display: flex; align-items: center; justify-content: center; gap: 40px;
  }
  .card {
    width: 540px; height: 310px; position: relative;
    box-shadow: 0 6px 18px rgba(0,0,0,.25);
  }
  /* Front */
  .card--front { background: var(--card-white); }
  .holder {
    position: absolute; right: 290px; top: 128px; text-align: right;
  }
  .holder__name {
    font-family: "Open Sans", sans-serif; font-weight: 700;
    font-size: 19px; color: var(--name-blue); letter-spacing: -.3px; white-space: nowrap;
  }
  .holder__role {
    font-family: "Arimo", sans-serif; font-size: 13px; color: var(--text-grey); margin-top: 2px;
  }
  .divider {
    position: absolute; left: 262px; top: 70px; width: 1.5px; height: 150px;
    background: var(--icon-blue);
  }
  .contact {
    position: absolute; left: 278px; top: 64px;
    font-family: "Arimo", sans-serif; font-size: 12.5px; color: var(--text-grey); line-height: 17px;
  }
  .contact__address { margin-bottom: 4px; }
  .contact__list { list-style: none; }
  .contact__list li { display: flex; align-items: center; gap: 6px; }
  .contact__list svg { width: 11px; height: 11px; flex: none; fill: var(--icon-blue); }
  /* Back */
  .card--back { background: var(--brand-blue); color: var(--on-blue); }
  .brand {
    position: absolute; left: 0; right: 0; top: 100px;
    display: flex; align-items: center; justify-content: center; gap: 12px;
  }
  .brand__dot {
    width: 22px; height: 22px; border-radius: 50%; background: var(--silver);
  }
  .brand__name {
    font-family: "Arimo", sans-serif; font-size: 30px; letter-spacing: 3px;
    color: var(--silver); white-space: nowrap;
  }
  .tagline {
    position: absolute; left: 30px; right: 24px; bottom: 32px;
    font-family: "Arimo", sans-serif; font-size: 14px; color: var(--on-blue);
  }
</style>
</head>
<body>
<main class="stage">
  <section class="card card--front" aria-label="Cara delantera">
    <div class="holder">
      <p class="holder__name">MARTÍN SOSA RIVERA</p>
      <p class="holder__role">Comercial</p>
    </div>
    <div class="divider"></div>
    <div class="contact">
      <p class="contact__address">Pol. Ind. Norvalle-C/4 Nº 12<br>41720 VILLAVERDE DEL RÍO (Sevilla)<br>Apartado de Correos 264</p>
      <ul class="contact__list">
        <li><svg viewBox="0 0 12 12"><path d="M3 0h6a1 1 0 0 1 1 1v10a1 1 0 0 1-1 1H3a1 1 0 0 1-1-1V1a1 1 0 0 1 1-1zm0 1.5v8h6v-8z"/></svg>611 42 57 80</li>
        <li><svg viewBox="0 0 12 12"><path d="M2.5 0.5l2 2.5-1.2 1.3a7 7 0 0 0 4.4 4.4L9 7.5l2.5 2-1.5 2C5 11.5 0.5 7 0.5 2z"/></svg>954 20 18 47</li>
        <li><svg viewBox="0 0 12 12"><path d="M3 0h6v3H3zM1 4h10v5H9v3H3V9H1zm3 4v3h4V8z"/></svg>954 20 18 52</li>
        <li><svg viewBox="0 0 12 12"><path d="M0 2h12v8H0zm1 1v.4l5 3.3 5-3.3V3z"/></svg>martinsosa@travenic.com</li>
        <li><svg viewBox="0 0 12 12"><circle cx="6" cy="6" r="5.5"/></svg>www.travenic.com</li>
      </ul>
    </div>
  </section>

  <section class="card card--back" aria-label="Cara trasera">
    <div class="brand">
      <span class="brand__dot"></span>
      <span class="brand__name">TRAVENIC EXTRUSION</span>
    </div>
    <p class="tagline">Diseño, extrusion, lacado, anodizado y mecanizado de precisión de aluminio</p>
  </section>
</main>
</body>
</html>
```